Aerospace Private Equity Firm Needs Website

We need a website for new private equity fund called Orlin Partners. We buy smaller companies in the aerospace and industrial industries. I have attached some information about the firm. An example of a site we like that is a similar business but focused in a different sector is www.travomedic.com. www.quarnestgrove.com is a firm that also invests in aerospace companies.

Industry/Entity Type

Equity

Number of Pages Required

1 page

Colors
0555a3
33a6d7
ec1f27

```html
<!DOCTYPE html>
<html lang="en">
<head>
<meta charset="utf-8">
<title>Orlin Partners</title>
<link href="https://fonts.googleapis.com/css2?family=Roboto:wght@300;400&display=swap" rel="stylesheet">
<style>
:root{
  --navy:#0a3b8f;
  --red:#c80a0a;
  --page:#f7f7f7;
  --ink:#333;
  --card-line:#3d63a8;
  --hero-a:#0d2f6e;
  --hero-b:#3f7fbf;
}
*{box-sizing:border-box;margin:0;padding:0}
html,body{width:1200px;height:1198px;overflow:hidden}
body{background:var(--page);font-family:'Roboto',sans-serif;color:var(--ink);position:relative;border-top:2px solid var(--red)}
.site-header{height:143px;position:relative}
.brand{position:absolute;left:120px;top:44px;display:flex;align-items:center;gap:10px}
.brand-mark{width:14px;height:14px;background:var(--red)}
.brand-name{font-size:34px;font-weight:400;color:var(--navy);letter-spacing:.5px}
.header-actions{position:absolute;top:55px;left:790px;display:flex;gap:5px}
.btn-top{height:37px;display:flex;align-items:center;justify-content:center;color:#fff;font-size:16px;font-weight:400}
.btn-login{width:102px;background:var(--navy)}
.btn-overview{width:182px;background:var(--red)}
.main-nav{height:45px;background:var(--navy);display:flex;padding-left:190px}
.main-nav a{color:#fff;text-decoration:none;font-size:16px;display:flex;align-items:center;justify-content:center;height:45px}
.main-nav a.active{background:var(--red)}
.hero{height:348px;background:radial-gradient(ellipse at 58% 50%,#5d9fd6 0%,var(--hero-b) 30%,var(--hero-a) 100%)}
.intro{text-align:center;font-weight:300;font-size:19.5px;line-height:25.6px;color:#333;margin:34px auto 0;width:840px}
.cards{position:absolute;top:704px;left:120px;display:flex;gap:28px}
.card{width:301px;height:361px;border:1px solid var(--card-line);position:relative}
.card-logo{position:absolute;top:50px;left:47px;display:flex;align-items:center;gap:7px}
.card-logo-mark{width:14px;height:14px;background:var(--navy)}
.card-logo-name{font-size:16px;font-weight:400;color:#555}
.card-text{position:absolute;top:135px;left:29px;right:26px;font-size:18px;font-weight:300;line-height:23.3px;color:#333}
.card-btn{position:absolute;top:284px;left:30px;width:238px;height:49px;border:1px solid var(--red);color:var(--red);display:flex;align-items:center;justify-content:center;font-size:16px}
.card-btn.is-hover{border-color:var(--navy);color:var(--navy)}
.site-footer{position:absolute;left:0;top:1109px;width:1200px;height:89px;background:var(--red);color:#fff}
.legal{position:absolute;left:120px;top:37px;font-size:10px;font-weight:300}
.footer-brand{position:absolute;right:120px;top:28px;font-size:20px;font-weight:400}
</style>
</head>
<body>
<header class="site-header">
  <div class="brand"><span class="brand-mark"></span><span class="brand-name">Orlin Partners</span></div>
  <div class="header-actions">
    <span class="btn-top btn-login">LOG IN</span>
    <span class="btn-top btn-overview">FIRM OVERVIEW</span>
  </div>
</header>
<nav class="main-nav">
  <a class="active" style="width:110px">HOME</a>
  <a style="width:112px">ABOUT</a>
  <a style="width:110px">STRATEGY</a>
  <a style="width:133px">INVESTMENTS</a>
  <a style="width:133px">TEAM</a>
  <a style="width:78px">NEWS</a>
  <a style="width:142px">CONTACT</a>
</nav>
<div class="hero" role="img" aria-label="Hand touching a glowing financial data interface with charts"></div>
<p class="intro">Orlin Partners (“Orlin”) is a Los Angeles, California-based private equity firm formed in 2016 by Principals from Westmere Park Associates (WPA). Orlin focuses on lower middle-market control investments in aerospace and industrial companies based in North America.<br>The Orlin team has invested successfully in these sectors over a 10-year period while at WPA.</p>
<section class="cards">
  <article class="card">
    <div class="card-logo"><span class="card-logo-mark"></span><span class="card-logo-name">Halvern Aerospace, Inc.</span></div>
    <p class="card-text">Daniel Marsh joined Corvet Processing in 1996. At the time Corvet had revenues of $3 million. Marsh acquired control of the company in 2011.</p>
    <span class="card-btn">OUR INVESTORS</span>
  </article>
  <article class="card">
    <div class="card-logo"><span class="card-logo-mark"></span><span class="card-logo-name">Halvern Aerospace, Inc.</span></div>
    <p class="card-text">Daniel Marsh joined Corvet Processing in 1996. At the time Corvet had revenues of $3 million. Marsh acquired control of the company in 2011.</p>
    <span class="card-btn is-hover">OUR INVESTORS</span>
  </article>
  <article class="card">
    <div class="card-logo"><span class="card-logo-mark"></span><span class="card-logo-name">Halvern Aerospace, Inc.</span></div>
    <p class="card-text">Daniel Marsh joined Corvet Processing in 1996. At the time Corvet had revenues of $3 million. Marsh acquired control of the company in 2011.</p>
    <span class="card-btn">OUR INVESTORS</span>
  </article>
</section>
<footer class="site-footer">
  <p class="legal">© 2017 Orlin Partners Fund I, L.P. | Privacy Policy | User Agreement</p>
  <span class="footer-brand">Orlin Partners</span>
</footer>
</body>
</html>
```